" O Perito nomeado pelo Juiz do Trabalho agenda uma Perícia Trabalhista, pedindo para avaliar a Insalubridade ou Periculosidade que o Reclamante afirma existir, tanto o Reclamante como a Reclamada tem o direito de contratar um Assistente Técnico, é ai que entra o nosso serviço. site: www.rotaverdeassessoria.com "

```html
<!DOCTYPE html>
<html lang="pt-BR">
<head>
<meta charset="utf-8">
<title>Rota Verde Assessoria — Cartão de Visita</title>
<link href="https://fonts.googleapis.com/css2?family=Open+Sans:wght@300;400;600&display=swap" rel="stylesheet">
<style>
  :root {
    --bg: #2a2a2c;
    --card-black: #141414;
    --card-black-2: #1c1c1c;
    --card-white: #ffffff;
    --pattern-white: #f1f1f1;
    --gold: #c9a24a;
    --gold-light: #e8cf8a;
    --gold-dark: #8a6a25;
    --text-light: #f2f2f2;
    --text-muted: #bdbdbd;
    --grey-band: #6d6d6d;
  }
  * { box-sizing: border-box; margin: 0; padding: 0; }
  html, body {
    width: 1200px; height: 1200px; overflow: hidden;
    background: var(--bg);
    font-family: "Open Sans", Arial, sans-serif;
  }
  .canvas {
    width: 1200px; height: 1200px;
    display: flex; flex-direction: column; align-items: center; justify-content: center;
    gap: 70px;
  }
  .card {
    width: 900px; height: 510px; border-radius: 26px; overflow: hidden;
    position: relative;
    box-shadow: 0 18px 40px rgba(0,0,0,.45);
  }

  /* Front */
  .card-front {
    background: radial-gradient(ellipse at center, var(--card-black-2), var(--card-black) 75%);
  }
  .front-texture {
    position: absolute; inset: 0;
    background: linear-gradient(135deg, #181818, #121212);
  }
  .front-frame {
    position: absolute; left: 150px; top: 75px; width: 600px; height: 360px;
    border: 3px solid var(--gold);
  }
  .front-brand {
    position: absolute; left: 50%; top: 50%; transform: translate(-50%, -50%);
    display: flex; align-items: center; gap: 26px;
  }
  .brand-square {
    width: 62px; height: 62px; background: var(--gold);
  }
  .brand-text { display: flex; flex-direction: column; }
  .brand-name {
    color: var(--gold); font-weight: 600; font-size: 44px; line-height: 1.05;
    letter-spacing: 2px; text-transform: uppercase;
  }
  .brand-tag {
    color: var(--gold); font-weight: 600; font-size: 14px; letter-spacing: 5px;
    text-transform: uppercase; margin-top: 8px;
  }

  /* Back */
  .card-back { display: flex; background: var(--card-black); }
  .back-left {
    width: 44%; background: var(--card-white);
    display: flex; align-items: center; justify-content: center;
    position: relative;
  }
  .back-left .brand-square { width: 40px; height: 40px; }
  .back-left .brand-name { font-size: 28px; }
  .back-left .brand-tag { font-size: 10px; letter-spacing: 3px; }
  .back-left .front-brand { position: static; transform: none; gap: 16px; }
  .back-right {
    flex: 1; position: relative; padding: 60px 0 0 46px; color: var(--text-light);
  }
  .person-name { font-size: 34px; font-weight: 300; }
  .person-role { font-size: 19px; font-weight: 300; color: var(--text-muted); margin-top: 2px; }
  .contact-list { list-style: none; margin-top: 46px; }
  .contact-item {
    display: flex; align-items: flex-start; gap: 16px;
    font-size: 17px; color: var(--text-light); margin-bottom: 16px; line-height: 1.35;
  }
  .contact-icon { width: 20px; height: 20px; flex: none; margin-top: 2px; }
  .site-band {
    position: absolute; left: -396px; right: 0; bottom: 0; height: 86px;
    display: flex; align-items: center; justify-content: flex-end; padding-right: 60px;
    background: linear-gradient(to bottom, var(--card-black) 0, var(--card-black) 70%, var(--grey-band) 70%);
  }
  .site-url { color: var(--text-light); font-size: 22px; font-weight: 400; margin-bottom: 26px; }
  .gold-rule {
    position: absolute; left: -396px; right: 0; bottom: 26px; height: 3px; background: var(--gold);
  }
</style>
</head>
<body>
<main class="canvas">

  <section class="card card-front" aria-label="Frente do cartão">
    <div class="front-texture" role="img" aria-label="Textura geométrica discreta em preto"></div>
    <div class="front-frame"></div>
    <div class="front-brand">
      <div class="brand-square"></div>
      <div class="brand-text">
        <span class="brand-name">Rota Verde</span>
        <span class="brand-tag">Assessoria Técnica</span>
      </div>
    </div>
  </section>

  <section class="card card-back" aria-label="Verso do cartão">
    <div class="back-left">
      <div class="front-brand">
        <div class="brand-square"></div>
        <div class="brand-text">
          <span class="brand-name">Rota Verde</span>
          <span class="brand-tag">Assessoria Técnica</span>
        </div>
      </div>
    </div>
    <div class="back-right">
      <h1 class="person-name">Nome Completo</h1>
      <p class="person-role">Cargo</p>
      <ul class="contact-list">
        <li class="contact-item">
          <svg class="contact-icon" viewBox="0 0 24 24" fill="var(--gold)"><path d="M6.6 10.8a15 15 0 0 0 6.6 6.6l2.2-2.2c.3-.3.7-.4 1-.2 1.1.4 2.3.6 3.6.6.6 0 1 .4 1 1V20c0 .6-.4 1-1 1C10.6 21 3 13.4 3 4c0-.6.4-1 1-1h3.5c.6 0 1 .4 1 1 0 1.3.2 2.5.6 3.6.1.3 0 .7-.2 1z"/></svg>
          <span>(xx) xxxx-xxxx</span>
        </li>
        <li class="contact-item">
          <svg class="contact-icon" viewBox="0 0 24 24" fill="var(--gold)"><path d="M12 2a7 7 0 0 0-7 7c0 5.2 7 13 7 13s7-7.8 7-13a7 7 0 0 0-7-7zm0 9.5A2.5 2.5 0 1 1 12 6.5a2.5 2.5 0 0 1 0 5z"/></svg>
          <span>Rua Seu Endereço, 324<br>Bairro - SP - CEP 000-0000</span>
        </li>
        <li class="contact-item">
          <svg class="contact-icon" viewBox="0 0 24 24" fill="var(--gold)"><path d="M3 5h18v14H3z" fill="none" stroke="var(--gold)" stroke-width="2"/><path d="M3 5l9 7 9-7" fill="none" stroke="var(--gold)" stroke-width="2"/></svg>
          <span>contato@rotaverde.com</span>
        </li>
      </ul>
      <div class="site-band">
        <span class="site-url">www.rotaverdeassessoria.com</span>
      </div>
      <div class="gold-rule"></div>
    </div>
  </section>

</main>
</body>
</html>
```